Toravel Project Consulting

I need a logo and business card design for a small business operating in the management consulting and contractor space, predominantly in local and state government. I specialise in project management, financial consulting, people and culture, procurement, ICT transformation and contracting for corporate support areas of organisations.

Industry/Entity Type

Business

```html
<!DOCTYPE html>
<html lang="en">
<head>
<meta charset="utf-8">
<title>Toravel Project Consulting – Business Card</title>
<link rel="stylesheet" href="https://fonts.googleapis.com/css2?family=Cabin:wght@400;500&display=swap">
<style>
  :root {
    --slate: #6d7a7a;
    --orange: #ff9500;
    --paper: #ffffff;
    --shadow: rgba(0, 0, 0, 0.55);
  }
  * { margin: 0; padding: 0; box-sizing: border-box; }
  html, body {
    width: 1003px;
    height: 1200px;
    overflow: hidden;
    background: var(--paper);
  }
  .canvas {
    position: relative;
    width: 1003px;
    height: 1200px;
    font-family: "Cabin", "Gill Sans", sans-serif;
  }
  .card {
    position: absolute;
    left: 52px;
    width: 849px;
    height: 498px;
    overflow: hidden;
    box-shadow: 14px 18px 26px var(--shadow);
  }

  /* Front */
  .card--front { top: 50px; background: var(--slate); }
  .front__wordmark {
    position: absolute;
    left: 84px;
    top: 150px;
    display: flex;
    align-items: center;
    gap: 16px;
    font-size: 34px;
    font-weight: 500;
    line-height: 1;
    color: var(--paper);
    white-space: nowrap;
  }
  .brand-square {
    width: 36px;
    height: 36px;
    background: var(--orange);
  }
  .front__identity {
    position: absolute;
    right: 80px;
    top: 124px;
    text-align: right;
    color: var(--paper);
    white-space: nowrap;
  }
  .front__name { font-size: 60px; font-weight: 400; line-height: 1; }
  .front__role { font-size: 31px; font-weight: 400; margin-top: 14px; line-height: 1; }

  .front__band {
    position: absolute;
    left: 0;
    top: 362px;
    width: 100%;
    height: 136px;
    background: var(--orange);
  }
  .front__tab {
    position: absolute;
    left: 368px;
    top: 330px;
    width: 438px;
    height: 60px;
    background: var(--orange);
    border-radius: 44px 44px 0 0;
  }
  .front__address {
    position: absolute;
    left: 62px;
    top: 384px;
    color: var(--paper);
    font-size: 24px;
    font-style: normal;
    line-height: 35px;
    white-space: nowrap;
  }
  .front__contact {
    position: absolute;
    right: 80px;
    top: 362px;
    color: var(--paper);
    text-align: right;
    white-space: nowrap;
  }
  .contact-line {
    display: flex;
    justify-content: flex-end;
    align-items: center;
    gap: 14px;
    line-height: 1;
  }
  .contact-line--phone { font-size: 32px; }
  .contact-line--email { font-size: 29px; margin-top: 18px; }
  .contact-line svg { display: block; }

  /* Back */
  .card--back { top: 600px; background: var(--orange); }
  .back__band {
    position: absolute;
    left: 0;
    top: 168px;
    width: 100%;
    height: 166px;
    background: var(--slate);
    display: flex;
    align-items: center;
    padding-left: 62px;
    gap: 60px;
  }
  .back__square {
    flex: none;
    width: 108px;
    height: 108px;
    background: var(--orange);
  }
  .back__wordmark {
    font-size: 40px;
    font-weight: 500;
    line-height: 1;
    color: var(--paper);
    white-space: nowrap;
  }
</style>
</head>
<body>
<main class="canvas">
  <section class="card card--front" aria-label="Business card front">
    <div class="front__wordmark">
      <span class="brand-square"></span>
      <span>Toravel</span>
    </div>
    <div class="front__identity">
      <h1 class="front__name">Daniel Reeve</h1>
      <p class="front__role">Director</p>
    </div>
    <div class="front__tab"></div>
    <div class="front__band"></div>
    <address class="front__address">
      14 Harlow Parade<br>
      Westmere NSW 2071
    </address>
    <div class="front__contact">
      <p class="contact-line contact-line--phone">
        <svg width="20" height="30" viewBox="0 0 20 30" aria-hidden="true">
          <rect x="2" y="1.5" width="16" height="27" rx="3" fill="none" stroke="#fff" stroke-width="3"/>
          <rect x="5" y="5" width="10" height="15" fill="#fff"/>
          <circle cx="10" cy="24" r="1.8" fill="#fff"/>
        </svg>
        <span>9123 45678</span>
      </p>
      <p class="contact-line contact-line--email">
        <svg width="30" height="22" viewBox="0 0 30 22" aria-hidden="true">
          <rect x="1.5" y="1.5" width="27" height="19" fill="none" stroke="#fff" stroke-width="2.5"/>
          <polyline points="2,2 15,13 28,2" fill="none" stroke="#fff" stroke-width="2.5"/>
        </svg>
        <span>mail@toravel.com.au</span>
      </p>
    </div>
  </section>

  <section class="card card--back" aria-label="Business card back">
    <div class="back__band">
      <span class="back__square"></span>
      <span class="back__wordmark">Toravel Project Consulting</span>
    </div>
  </section>
</main>
</body>
</html>
```